Order Form Template

We are looking to develop a professional looking order form, also see attached a brochure of our solution to see how nice it is from the brochure, I also attached devices logos. I would like to have the devices nd plans in multiple lines and quantity and price and total price. also leave a space below for a policy of billing and cancellation which we will add ourself later.

```html
<!DOCTYPE html>
<html lang="en">
<head>
<meta charset="utf-8">
<title>Payment Authorization Form</title>
<link href="https://fonts.googleapis.com/css2?family=Montserrat:wght@400;500;600;700&display=swap" rel="stylesheet">
<style>
  :root {
    --blue: #3689b8;
    --blue-text: #2f7fb0;
    --blue-light: #b7deee;
    --white: #ffffff;
    --backdrop: #e8e9eb;
    --dot: #c9c9c9;
  }
  * { box-sizing: border-box; margin: 0; padding: 0; }
  html, body { width: 1200px; height: 912px; overflow: hidden; }
  body {
    background: var(--backdrop);
    font-family: "Montserrat", sans-serif;
    position: relative;
  }
  .page {
    position: absolute;
    top: 93px;
    width: 560px;
    height: 725px;
    background: var(--white);
    box-shadow: 0 4px 14px rgba(0,0,0,0.12);
    overflow: hidden;
  }
  .page--front { left: 20px; }
  .page--back { left: 620px; }

  .page-head { position: absolute; left: 0; top: 0; width: 560px; height: 89px; }
  .page-head svg { position: absolute; left: 0; top: 0; }
  .brand {
    position: absolute; left: 30px; top: 29px;
    display: flex; align-items: center; gap: 8px;
  }
  .brand-mark { width: 30px; height: 30px; border-radius: 50%; background: var(--blue); }
  .brand-name { font-size: 16px; font-weight: 600; color: var(--blue); letter-spacing: 0.2px; }
  .company-info {
    position: absolute; right: 31px; top: 17px;
    text-align: right; color: var(--white);
    font-size: 10.5px; line-height: 14.2px; font-weight: 400;
  }
  .company-info strong { font-weight: 700; }

  .title-band {
    position: absolute; left: 0; top: 89px; width: 560px; height: 32px;
    background: var(--blue); color: var(--white);
    font-size: 13px; font-weight: 700; letter-spacing: 0.2px;
    display: flex; align-items: center; justify-content: center;
  }

  .form-block {
    position: absolute; left: 33px; width: 494px;
    display: grid; gap: 1px;
    background: var(--blue); border: 1px solid var(--blue);
    font-size: 9px; font-weight: 700; color: var(--blue-text);
  }
  .block-title {
    grid-column: 1 / -1; background: var(--blue); color: var(--white);
    font-size: 11.5px; font-weight: 700;
    display: flex; align-items: center; justify-content: center;
  }
  .cell { background: var(--white); padding: 4px 5px; }
  .cell--label { background: var(--blue-light); display: flex; align-items: center; justify-content: center; }
  .cell--left { justify-content: flex-start; padding-left: 16px; }
  .cell--tint { background: var(--blue-light); }
  .cell--center { text-align: center; }

  .contact { top: 141px; grid-template-columns: 2fr 1fr 1fr 1fr 1fr 0fr; grid-template-columns: repeat(6, 1fr); grid-template-rows: 19px 17px 17px 17px 17px; }
  .contact .span-2 { grid-column: span 2; }
  .contact .span-6 { grid-column: span 6; }

  .method { top: 245px; grid-template-columns: 3fr 1fr 1fr 1fr; grid-template-rows: 19px 30px; }
  .method .cell { padding: 3px 8px; }

  .card { top: 310px; grid-template-columns: 1fr 1fr; grid-template-rows: 19px repeat(4, 16.5px); }
  .card .cell { padding: 2px 5px; display: flex; align-items: center; }

  .products { grid-template-columns: 1fr 1fr 1fr; }
  .products--front { top: 415px; grid-template-rows: 19px repeat(3, 53px 26px); }
  .products--back { top: 141px; grid-template-rows: repeat(3, 53px 26px) 99px 39px 39px 100px; }
  .products .device { grid-row: span 2; }
  .products .details { grid-column: span 2; }
  .products .split { display: grid; grid-template-columns: 1fr 1fr; gap: 1px; background: var(--blue); grid-column: span 2; padding: 0; }
  .products .split .cell { background: var(--white); }
  .products .price { background: var(--blue-light); display: flex; align-items: center; }

  .plans { grid-column: span 2; padding: 10px 5px; font-size: 11px; line-height: 17.6px; }
  .plan-item { display: flex; align-items: center; gap: 4px; }
  .plan-item svg { flex: none; }
  .full { grid-column: 1 / -1; }
  .halves { grid-column: 1 / -1; display: grid; grid-template-columns: 1fr 1fr; gap: 1px; background: var(--blue); }
  .halves .cell { background: var(--white); }

  .page-foot {
    position: absolute; left: 0; top: 700px; width: 560px; height: 25px;
    background: var(--blue); color: var(--white);
    font-size: 9.5px; font-weight: 700;
    display: flex; align-items: center; justify-content: center;
  }
</style>
</head>
<body>

<!-- Front sheet -->
<article class="page page--front">
  <header class="page-head">
    <svg width="560" height="89" viewBox="0 0 560 89">
      <polygon points="384,0 560,0 560,89 345,89" fill="var(--blue)"/>
      <g fill="var(--dot)">
        <circle cx="257" cy="31" r="1.8"/><circle cx="273" cy="31" r="1.8"/><circle cx="288" cy="31" r="1.8"/><circle cx="304" cy="31" r="1.8"/><circle cx="320" cy="31" r="1.8"/><circle cx="335" cy="31" r="1.8"/>
        <circle cx="257" cy="43" r="1.8"/><circle cx="273" cy="43" r="1.8"/><circle cx="288" cy="43" r="1.8"/><circle cx="304" cy="43" r="1.8"/><circle cx="320" cy="43" r="1.8"/><circle cx="335" cy="43" r="1.8"/>
        <circle cx="257" cy="54" r="1.8"/><circle cx="273" cy="54" r="1.8"/><circle cx="288" cy="54" r="1.8"/><circle cx="304" cy="54" r="1.8"/><circle cx="320" cy="54" r="1.8"/><circle cx="335" cy="54" r="1.8"/>
      </g>
    </svg>
    <div class="brand"><span class="brand-mark"></span><span class="brand-name">SUMMIT TRACK GPS</span></div>
    <address class="company-info" style="font-style:normal">
      <strong>Summit Track GPS Ltd.</strong><br>
      418 Rue des Pins, Quebec<br>
      H2X 4B7 Canada<br>
      1800 555 0147
    </address>
  </header>
  <div class="title-band">PAYMENT AUTHORIZATION</div>

  <section class="form-block contact">
    <div class="block-title">Customer Contact Information</div>
    <div class="cell cell--label span-2">Customer Company Name</div>
    <div class="cell cell--label span-2">Billing Contact Name</div>
    <div class="cell cell--label span-2">Billing E-Mail Address</div>
    <div class="cell span-6"></div>
    <div class="cell cell--label span-2 cell--left">Billing Address</div>
    <div class="cell cell--label">City</div>
    <div class="cell cell--label">State</div>
    <div class="cell cell--label">Zip Code</div>
    <div class="cell cell--label">Phone</div>
    <div class="cell span-6"></div>
  </section>

  <section class="form-block method">
    <div class="block-title">Payment Information</div>
    <div class="cell">Select Payment Method</div>
    <div class="cell cell--center">NorthCard</div>
    <div class="cell cell--center">Crestline</div>
    <div class="cell cell--center">Vireo Pay</div>
  </section>

  <section class="form-block card">
    <div class="block-title">PAYMENT INFORMATION – Fill only If paid by credit card</div>
    <div class="cell">Name on Credit Card as it Appears</div><div class="cell"></div>
    <div class="cell">Credit Card Number</div><div class="cell"></div>
    <div class="cell">Expiration Date</div><div class="cell"></div>
    <div class="cell">Credit Card Billing Address</div><div class="cell"></div>
  </section>

  <section class="form-block products products--front">
    <div class="block-title">PAYMENT INFORMATION – Fill only If paid by credit card</div>
    <div class="cell device"></div>
    <div class="cell details">Product Details:</div>
    <div class="cell price">Price :</div><div class="cell price">Quantity :</div>
    <div class="cell device"></div>
    <div class="cell details">Product Details:</div>
    <div class="cell price">Price :</div><div class="cell price">Price :</div>
    <div class="cell device"></div>
    <div class="cell details">Product Details:</div>
    <div class="cell price">Price :</div><div class="cell price">Quantity :</div>
  </section>

  <footer class="page-foot">www.summittrackgps.com</footer>
</article>

<!-- Back sheet -->
<article class="page page--back">
  <header class="page-head">
    <svg width="560" height="89" viewBox="0 0 560 89">
      <polygon points="384,0 560,0 560,89 345,89" fill="var(--blue)"/>
      <g fill="var(--dot)">
        <circle cx="257" cy="31" r="1.8"/><circle cx="273" cy="31" r="1.8"/><circle cx="288" cy="31" r="1.8"/><circle cx="304" cy="31" r="1.8"/><circle cx="320" cy="31" r="1.8"/><circle cx="335" cy="31" r="1.8"/>
        <circle cx="257" cy="43" r="1.8"/><circle cx="273" cy="43" r="1.8"/><circle cx="288" cy="43" r="1.8"/><circle cx="304" cy="43" r="1.8"/><circle cx="320" cy="43" r="1.8"/><circle cx="335" cy="43" r="1.8"/>
        <circle cx="257" cy="54" r="1.8"/><circle cx="273" cy="54" r="1.8"/><circle cx="288" cy="54" r="1.8"/><circle cx="304" cy="54" r="1.8"/><circle cx="320" cy="54" r="1.8"/><circle cx="335" cy="54" r="1.8"/>
      </g>
    </svg>
    <div class="brand"><span class="brand-mark"></span><span class="brand-name">SUMMIT TRACK GPS</span></div>
    <address class="company-info" style="font-style:normal">
      <strong>Summit Track GPS Ltd.</strong><br>
      418 Rue des Pins, Quebec<br>
      H2X 4B7 Canada<br>
      1800 555 0147
    </address>
  </header>
  <div class="title-band">PAYMENT AUTHORIZATION</div>

  <section class="form-block products products--back">
    <div class="cell device"></div>
    <div class="cell details">Product Details:</div>
    <div class="cell price">Price :</div><div class="cell price">Quantity :</div>
    <div class="cell device"></div>
    <div class="cell details">Product Details:</div>
    <div class="cell price">Price :</div><div class="cell price">Quantity :</div>
    <div class="cell device"></div>
    <div class="split"><div class="cell"></div><div class="cell"></div></div>
    <div class="cell price">Price :</div><div class="cell price">Quantity :</div>
    <div class="cell"></div>
    <div class="cell plans">
      <div>Monthly Plan: (Please check off)</div>
      <div class="plan-item"><svg width="9" height="9" viewBox="0 0 9 9"><rect x="0.5" y="0.5" width="8" height="8" fill="none" stroke="var(--blue-text)"/></svg>Base Plan, $24.99 per unit</div>
      <div class="plan-item"><svg width="9" height="9" viewBox="0 0 9 9"><rect x="0.5" y="0.5" width="8" height="8" fill="none" stroke="var(--blue-text)"/></svg>Pro Plan, $34.99 per unit</div>
      <div class="plan-item"><svg width="9" height="9" viewBox="0 0 9 9"><rect x="0.5" y="0.5" width="8" height="8" fill="none" stroke="var(--blue-text)"/><path d="M2 2 7 7M7 2 2 7" stroke="var(--blue-text)"/></svg>ProPlus Plan, $39.99 per unit</div>
      <div class="plan-item"><svg width="9" height="9" viewBox="0 0 9 9"><rect x="0.5" y="0.5" width="8" height="8" fill="none" stroke="var(--blue-text)"/><path d="M2 2 7 7M7 2 2 7" stroke="var(--blue-text)"/></svg>Camera Plan, $29.99 per unit</div>
    </div>
    <div class="cell cell--tint full">Signature</div>
    <div class="halves"><div class="cell">Printed Name</div><div class="cell">Date</div></div>
    <div class="cell cell--tint full">NOTE</div>
  </section>

  <footer class="page-foot">www.summittrackgps.com</footer>
</article>

</body>
</html>
```